GUMMY MYLAR BAG PACKAGE DESIGN

The FRONT of the label needs a fresh look. We are hoping for clean/modern.

The information on the label is correct

We would like to make CBD more prominent also. And we love showing that the product is made in Michigan , we have an icon you're welcome to move or make different.

I'm excited to see , thank you !

Target Market(s)

Adult, health supplement

```html
<!DOCTYPE html>
<html lang="en">
<head>
<meta charset="utf-8">
<title>Kova's CBD Gummy Pouches</title>
<link href="https://fonts.googleapis.com/css2?family=Anton&family=Oswald:wght@500;600&display=swap" rel="stylesheet">
<style>
  :root {
    --backdrop: #e0cfba;
    --pouch: #f4f4f4;
    --pouch-edge: #e4e4e4;
    --ink: #111111;
    --paper: #ffffff;
    --brand-red: #e0323a;
    --leaf-green: #2e8b4a;
    --mint: #8fd8c8;
    --berry: #f19a9e;
    --rule: #444444;
  }
  * { box-sizing: border-box; margin: 0; padding: 0; }
  html, body { width: 1200px; height: 960px; overflow: hidden; }
  body { background: var(--backdrop); position: relative; font-family: "Oswald", sans-serif; color: var(--ink); }

  .pouch {
    position: absolute; top: 198px; width: 421px; height: 609px;
    background: var(--pouch); border-radius: 16px; overflow: hidden;
    box-shadow: inset 0 0 0 1px var(--pouch-edge);
  }
  .pouch--butterfly { left: 157px; }
  .pouch--bear { left: 632px; }

  .pouch__zipper { position: absolute; left: 22px; right: 22px; top: 45px; height: 4px; background: var(--pouch-edge); border-radius: 2px; }

  .pouch__contents { position: absolute; left: 16px; top: 192px; width: 389px; height: 345px; border-radius: 40px; filter: blur(14px); opacity: .75; }
  .pouch--butterfly .pouch__contents { background: radial-gradient(ellipse at center, var(--mint), rgba(143,216,200,0.2)); }
  .pouch--bear .pouch__contents { background: radial-gradient(ellipse at center, var(--berry), rgba(241,154,158,0.2)); }

  .brand__dot { position: absolute; left: 50%; top: 80px; width: 40px; height: 40px; margin-left: -20px; border-radius: 50%; background: var(--leaf-green); }
  .brand__name { position: absolute; left: 0; right: 0; top: 126px; text-align: center; font-family: "Anton", sans-serif; font-size: 64px; line-height: 1; letter-spacing: 3px; color: var(--brand-red); }

  .hero { position: absolute; left: 71px; top: 206px; width: 279px; height: 211px; background: var(--ink); border-radius: 60px 60px 70px 70px; }
  .hero__title { position: absolute; left: 71px; width: 279px; text-align: center; font-family: "Oswald", sans-serif; font-weight: 600; color: var(--paper); line-height: 1; transform: scaleY(1.2); }
  .pouch--butterfly .hero__title--a { top: 272px; font-size: 50px; }
  .pouch--butterfly .hero__title--b { top: 334px; font-size: 50px; }
  .pouch--bear .hero__title--a { top: 264px; font-size: 26px; }
  .pouch--bear .hero__title--b { top: 298px; font-size: 46px; }
  .pouch--bear .hero__title--c { top: 350px; font-size: 46px; }

  .badge-state { position: absolute; left: 21px; top: 328px; width: 68px; height: 68px; border-radius: 50%; background: var(--paper); border: 6px solid var(--ink); }
  .badge-icon { position: absolute; left: 359px; width: 36px; height: 36px; border-radius: 50%; background: var(--ink); box-shadow: inset 0 0 0 3px var(--ink), inset 0 0 0 4px var(--paper); }
  .badge-icon--1 { top: 288px; } .badge-icon--2 { top: 344px; } .badge-icon--3 { top: 399px; }

  .product-line { position: absolute; left: 0; right: 0; top: 420px; text-align: center; font-family: "Anton", sans-serif; font-size: 58px; line-height: 1; letter-spacing: 1px; }

  .dose { position: absolute; left: 88px; top: 481px; width: 245px; height: 49px; border-top: 1px solid var(--rule); border-bottom: 1px solid var(--rule); display: flex; }
  .dose__total { width: 117px; border-right: 1px solid var(--rule); text-align: center; padding-top: 2px; }
  .dose__each { flex: 1; text-align: center; padding-top: 5px; font-size: 15px; font-weight: 600; line-height: 1.15; }
  .dose__label { font-size: 15px; font-weight: 500; line-height: 1; }
  .dose__amount { font-family: "Anton", sans-serif; font-size: 22px; line-height: 1.1; }

  .count { position: absolute; left: 20px; top: 546px; }
  .count__qty { font-size: 17px; font-weight: 600; line-height: 1; }
  .count__weight { font-size: 11px; font-weight: 500; line-height: 1.4; }
  .supplement { position: absolute; right: 19px; top: 552px; text-align: right; }
  .supplement__title { font-size: 14px; font-weight: 600; line-height: 1; }
  .supplement__note { font-size: 8.5px; font-weight: 500; line-height: 1.5; }
</style>
</head>
<body>

<section class="pouch pouch--butterfly">
  <div class="pouch__zipper"></div>
  <div class="pouch__contents" role="img" aria-label="Mint green butterfly gummies visible through the pouch"></div>
  <div class="brand__dot"></div>
  <div class="brand__name">KOVA'S</div>
  <div class="hero" role="img" aria-label="Black butterfly silhouette"></div>
  <div class="hero__title hero__title--a">BUTTERFLY</div>
  <div class="hero__title hero__title--b">GUMMIES</div>
  <div class="badge-state"></div>
  <div class="badge-icon badge-icon--1"></div>
  <div class="badge-icon badge-icon--2"></div>
  <div class="badge-icon badge-icon--3"></div>
  <div class="product-line">CBD GUMMY</div>
  <div class="dose">
    <div class="dose__total"><div class="dose__label">PACKAGE CONTAINS</div><div class="dose__amount">400 MG CBD</div></div>
    <div class="dose__each">APPROX. 20 MG CBD<br>PER BUTTERFLY</div>
  </div>
  <div class="count"><div class="count__qty">20 Gummies*</div><div class="count__weight">NET WT. 2.47oz (70G)</div></div>
  <div class="supplement"><div class="supplement__title">DIETARY SUPPLEMENT</div><div class="supplement__note">*APPROX. (PACKAGED BY WEIGHT)</div></div>
</section>

<section class="pouch pouch--bear">
  <div class="pouch__zipper"></div>
  <div class="pouch__contents" role="img" aria-label="Pink strawberry gummy bears visible through the pouch"></div>
  <div class="brand__dot"></div>
  <div class="brand__name">KOVA'S</div>
  <div class="hero" role="img" aria-label="Black silhouette of two gummy bears side by side"></div>
  <div class="hero__title hero__title--a">STRAWBERRY</div>
  <div class="hero__title hero__title--b">CBD GUMMY</div>
  <div class="hero__title hero__title--c">BEARS</div>
  <div class="badge-state"></div>
  <div class="badge-icon badge-icon--1"></div>
  <div class="badge-icon badge-icon--2"></div>
  <div class="badge-icon badge-icon--3"></div>
  <div class="product-line">CBD GUMMY</div>
  <div class="dose">
    <div class="dose__total"><div class="dose__label">PACKAGE CONTAINS</div><div class="dose__amount">250 MG CBD</div></div>
    <div class="dose__each">APPROX. 12.5 MG<br>CBD PER BUTTERFLY</div>
  </div>
  <div class="count"><div class="count__qty">20 Gummies*</div><div class="count__weight">NET WT. 2.47oz (70G)</div></div>
  <div class="supplement"><div class="supplement__title">DIETARY SUPPLEMENT</div><div class="supplement__note">*APPROX. (PACKAGED BY WEIGHT)</div></div>
</section>

</body>
</html>
```